Creative label for amber glass candle jar.

We are a candle company. Our products are handmade by us and natural. We are looking for something minimalistic and unique. We need a label for our candle jars (amber glass with black lid). Our current label doesn't match these requirements. We would like our products to be stocked in London shop, therefore design has to be up to a high standard. Jar specification Diameter (mm) 65 Height without cap (mm) 80. We want the new design to be different from the current one. It's just a guide for wording.
We should be able adjust the label, to change scent name.
Our scents are
*Coconut & Vanilla
*Lavender
*Bergamot
*Italian Garden
*Hygge
*Eucalyptus & Peppermint
*Coffee
*Cedarwood & Juniperberry
To know more about us, visit our website www.wrenfieldcandles.com or instagram.com/wrenfieldcandles
Good luck!
Industry/Entity Type
It Company
Colors
Designer to choose colors to be used in the design.
Requirements
Must have
- * I have attached two of our logos, label design must include one of them.
- *has to mention that it's made in London
- *has to say that candle is natural/made with essential oils
- *has to have scent name and No. on it..
- Label can be vertical or horizontal, but has to be square/rectangular,.
Should not have
- Label should not be round

```html
<!DOCTYPE html>
<html lang="en">
<head>
<meta charset="utf-8">
<title>wrenfield — candle label redesign, design 04</title>
<link rel="stylesheet" href="https://fonts.googleapis.com/css2?family=Share+Tech+Mono&display=swap">
<style>
  :root {
    --board-light: #e4e4e2;
    --board-mid: #d3d3d1;
    --paper: #e9c9ae;
    --paper-deep: #dfbb9d;
    --ink: #111111;
  }
  * { margin: 0; padding: 0; box-sizing: border-box; }
  html, body { width: 766px; height: 1200px; overflow: hidden; }
  body { font-family: "Share Tech Mono", monospace; color: var(--ink); }

  .board {
    position: relative;
    width: 766px;
    height: 1200px;
    overflow: hidden;
  }
  .board-surface {
    position: absolute;
    inset: 0;
    background: linear-gradient(180deg, var(--board-light), var(--board-mid) 50%, var(--board-light));
  }

  .board-title {
    position: absolute;
    left: 58px;
    top: 38px;
    font-size: 84px;
    line-height: 1;
    letter-spacing: 2px;
  }
  .board-subtitle {
    position: absolute;
    left: 131px;
    top: 130px;
    font-size: 25px;
    line-height: 30px;
    letter-spacing: 1px;
  }
  .board-version {
    position: absolute;
    left: 62px;
    top: 196px;
    font-size: 23px;
    letter-spacing: 1px;
  }

  .label {
    position: absolute;
    width: 312px;
    height: 364px;
    background: radial-gradient(ellipse at 40% 40%, var(--paper), var(--paper-deep));
  }
  .label--hygge    { left: 46px;  top: 297px; }
  .label--coconut  { left: 406px; top: 297px; }
  .label--italian  { left: 46px;  top: 714px; }
  .label--coffee   { left: 406px; top: 714px; }

  .scent-name {
    position: absolute;
    left: 19px;
    top: 18px;
    font-size: 37px;
    line-height: 36px;
    letter-spacing: 2px;
  }
  .label-brand {
    position: absolute;
    left: 20px;
    top: 100px;
    font-size: 24px;
    letter-spacing: 1px;
  }
  .label-claim {
    position: absolute;
    left: 20px;
    top: 132px;
    font-size: 12.5px;
    line-height: 14px;
  }
  .scent-number {
    position: absolute;
    right: 18px;
    bottom: 12px;
    font-size: 124px;
    line-height: 1;
    letter-spacing: 2px;
  }
</style>
</head>
<body>
  <main class="board">
    <div class="board-surface" role="img" aria-label="Whitewashed wooden plank backdrop"></div>

    <h1 class="board-title">wrenfield</h1>
    <p class="board-subtitle">candle label redesign</p>
    <p class="board-version">design 04</p>

    <section class="label label--hygge" role="group" aria-label="hygge label">
      <h2 class="scent-name">hygge</h2>
      <p class="label-brand">wrenfield</p>
      <p class="label-claim">handpoured in london using<br>natural essential oils</p>
      <p class="scent-number">05</p>
    </section>

    <section class="label label--coconut" role="group" aria-label="coconut and vanilla label">
      <h2 class="scent-name">coconut &amp;<br>vanilla</h2>
      <p class="label-brand">wrenfield</p>
      <p class="label-claim">handpoured in london using<br>natural essential oils</p>
      <p class="scent-number">01</p>
    </section>

    <section class="label label--italian" role="group" aria-label="italian garden label">
      <h2 class="scent-name">italian<br>garden</h2>
      <p class="label-brand">wrenfield</p>
      <p class="label-claim">handpoured in london using<br>natural essential oils</p>
      <p class="scent-number">04</p>
    </section>

    <section class="label label--coffee" role="group" aria-label="coffee label">
      <h2 class="scent-name">coffee</h2>
      <p class="label-brand">wrenfield</p>
      <p class="label-claim">handpoured in london using<br>natural essential oils</p>
      <p class="scent-number">07</p>
    </section>
  </main>
</body>
</html>
```